Interval Timer App

Need to have design for the attached wireframe. Similar app can be found here: https://shop.velmorix.net/market/apps/entry?ref=nx.brollwick.cyclecounter

```html
<!DOCTYPE html>
<html lang="en">
<head>
<meta charset="utf-8">
<title>Interval Timer – Quit Confirmation</title>
<link href="https://fonts.googleapis.com/css2?family=Open+Sans:wght@400;600&display=swap" rel="stylesheet">
<style>
  :root {
    --bg-top: #5e9a6c;
    --bg-bottom: #148f58;
    --blue: #1a7fe3;
    --ink: #222831;
    --card-dim: #a3a4a8;
    --control-dim: #aeafb3;
    --white: #ffffff;
  }
  * { box-sizing: border-box; margin: 0; padding: 0; }
  html, body { width: 675px; height: 1200px; overflow: hidden; }
  body {
    font-family: "Open Sans", sans-serif;
    background: linear-gradient(180deg, var(--bg-top) 0%, var(--bg-bottom) 100%);
    position: relative;
    color: var(--ink);
  }
  .back-button { position: absolute; left: 30px; top: 40px; width: 30px; height: 34px; }
  .set-label {
    position: absolute; top: 168px; left: 0; width: 100%;
    text-align: center; font-size: 20px; font-weight: 600; letter-spacing: 0.5px; color: var(--ink);
  }
  .progress {
    position: absolute; top: 214px; left: 197px; width: 285px; height: 4px;
    background: var(--white); border-radius: 2px;
  }
  .progress-fill { position: absolute; left: 0; top: 0; width: 122px; height: 4px; background: var(--blue); border-radius: 2px; }
  .progress-knob {
    position: absolute; left: 111px; top: -9px; width: 22px; height: 22px;
    border-radius: 50%; background: var(--white); border: 3px solid var(--blue);
  }
  .timer-card {
    position: absolute; left: 30px; top: 281px; width: 615px; height: 638px;
    background: var(--card-dim); border-radius: 18px;
  }
  .timer-title {
    position: absolute; top: 326px; left: 0; width: 100%;
    text-align: center; font-size: 40px; font-weight: 600; color: var(--ink);
  }
  .page-dot {
    position: absolute; left: 324px; top: 756px; width: 26px; height: 26px;
    border-radius: 50%; background: #174f8c;
  }
  .control {
    position: absolute; top: 796px; width: 102px; height: 102px; border-radius: 50%;
    background: var(--control-dim); box-shadow: 0 3px 8px rgba(0,0,0,0.18);
    display: flex; align-items: center; justify-content: center;
  }
  .control-restart { left: 48px; }
  .control-pause { left: 523px; }
  .dialog {
    position: absolute; left: 30px; top: 429px; width: 615px; height: 340px;
    background: var(--white); border-radius: 6px;
  }
  .dialog-title {
    position: absolute; top: 24px; left: 0; width: 100%; text-align: center;
    font-size: 33px; font-weight: 600; color: var(--ink);
  }
  .dialog-body {
    position: absolute; top: 130px; left: 0; width: 100%; text-align: center;
    font-size: 29px; font-weight: 400; color: var(--ink);
  }
  .dialog-button {
    position: absolute; top: 248px; width: 243px; height: 73px; border-radius: 37px;
    font-family: inherit; font-size: 25px; font-weight: 400; letter-spacing: 1px;
    display: flex; align-items: center; justify-content: center;
  }
  .button-yes { left: 19px; background: var(--white); color: var(--blue); border: 3px solid var(--blue); }
  .button-no { left: 353px; background: var(--blue); color: var(--white); border: none; }
</style>
</head>
<body>
  <svg class="back-button" viewBox="0 0 30 34" aria-label="Back">
    <polyline points="22,3 7,17 22,31" fill="none" stroke="#1d5f9e" stroke-width="4" stroke-linecap="round" stroke-linejoin="round"/>
  </svg>

  <div class="set-label">SET 1</div>
  <div class="progress">
    <div class="progress-fill"></div>
    <div class="progress-knob"></div>
  </div>

  <section class="timer-card"></section>
  <h1 class="timer-title">Work time!</h1>
  <div class="page-dot"></div>

  <div class="control control-restart">
    <svg width="50" height="50" viewBox="0 0 50 50" aria-label="Restart">
      <path d="M14 12 A18 18 0 1 0 30 8" fill="none" stroke="#1d5f9e" stroke-width="4" stroke-linecap="round"/>
      <polyline points="8,10 15,12 14,20" fill="none" stroke="#1d5f9e" stroke-width="4" stroke-linecap="round" stroke-linejoin="round"/>
    </svg>
  </div>
  <div class="control control-pause">
    <svg width="40" height="40" viewBox="0 0 40 40" aria-label="Pause">
      <rect x="10" y="8" width="4.5" height="24" rx="2" fill="#1d5f9e"/>
      <rect x="25.5" y="8" width="4.5" height="24" rx="2" fill="#1d5f9e"/>
    </svg>
  </div>

  <div class="dialog" role="dialog">
    <h2 class="dialog-title">Do you really want to quit?</h2>
    <p class="dialog-body">All your progress will be lost!</p>
    <button class="dialog-button button-yes">YES</button>
    <button class="dialog-button button-no">NO</button>
  </div>
</body>
</html>
```